Paint Protection Options

This is a flyer that will describe two different paint protection options for vehicles. I have mocked up a Word doc. As well, I've included some samples of other flyers where I like the "look". I am not locked into any single layout or design. In my Word doc I have them side-by-side. I think that makes sense but open to ideas. I've also added some pics of the two options being applied to cars. We need to have one of each (ceramic and ppf) at a minimum. In the grid I'm thinking different colors dots/circles to differentiate the different levels. But again, I'm open to suggestions. You can use the symbol for microns in the grid under the Thickness row. I spelled it out because I didn't know how to insert.

```html
<!DOCTYPE html>
<html lang="en">
<head>
<meta charset="utf-8">
<title>Paint Protection Options</title>
<link href="https://fonts.googleapis.com/css2?family=Oswald:wght@200;700&family=Poppins:wght@400;500;600;700&display=swap" rel="stylesheet">
<style>
  :root{
    --navy:#062d52;
    --blue:#1c5fae;
    --sky:#1f98dc;
    --steel:#6d9fc2;
    --slate:#4e7387;
    --ink:#1a1a1a;
    --card-light:#efefef;
    --card-dark:#e1e1e1;
    --cell:#d6e6f3;
    --cell-alt:#e7f0f8;
    --cell-last:#a9cfe8;
    --wax:#d99a5b;
    --wax-light:#efba80;
    --ppf:#a41212;
    --green:#52b51f;
    --yellow:#f7bf08;
    --red:#ee1111;
    --white:#ffffff;
  }
  *{box-sizing:border-box;margin:0;padding:0}
  html,body{width:909px;height:1200px;overflow:hidden;background:var(--white)}
  body{font-family:"Poppins",sans-serif;color:var(--ink);position:relative}

  .flyer{position:absolute;inset:0;background:var(--white);overflow:hidden}
  .hero-art{position:absolute;left:0;top:0;width:909px;height:540px}

  .title{position:absolute;left:57px;top:112px;font-family:"Oswald",sans-serif;
    font-size:92px;line-height:89px;letter-spacing:-2px;text-transform:uppercase}
  .title span{display:block;transform-origin:left center;white-space:nowrap}
  .title .t-paint{color:var(--white);font-weight:700;transform:scaleX(.82)}
  .title .t-protection{color:#000;font-weight:700;transform:scaleX(.8)}
  .title .t-options{color:var(--white);font-weight:200;transform:scaleX(.88)}

  .cards{position:absolute;left:58px;top:415px;width:799px;height:327px;border-radius:19px;
    overflow:hidden;display:flex}
  .card{position:relative;height:100%}
  .card-ceramic{width:405px;background:var(--card-light)}
  .card-ppf{width:394px;background:var(--card-dark)}
  .card h2{position:absolute;top:10px;font-size:20px;font-weight:700;letter-spacing:-.2px;
    line-height:24px;padding-bottom:2px;border-bottom:1px solid #9aa7b6;white-space:nowrap}
  .card h2 .accent{color:var(--blue)}
  .card-ceramic h2{left:24px}
  .card-ppf h2{left:22px;top:15px}
  .thumb{position:absolute;top:56px;width:100px;height:111px}
  .card-ceramic .thumb{left:24px}
  .card-ppf .thumb{left:24px}
  .lead{position:absolute;top:54px;font-size:10px;line-height:12.7px}
  .card-ceramic .lead{left:139px;width:246px}
  .card-ppf .lead{left:135px;width:240px}
  .body{position:absolute;top:183px;font-size:10px;line-height:12.7px}
  .card-ceramic .body{left:24px;width:365px}
  .card-ppf .body{left:19px;width:362px;top:180px}
  .ticks{position:absolute;list-style:none;font-size:10.5px;font-weight:600}
  .card-ceramic .ticks{left:24px;top:259px}
  .card-ppf .ticks{left:19px;top:256px}
  .ticks li{height:18px;display:flex;align-items:center;gap:11px}
  .ticks svg{width:9px;height:9px;flex:none}

  .compare{position:absolute;left:59px;top:762px;border-collapse:separate;border-spacing:3px 0;
    margin-left:-3px;table-layout:fixed}
  .compare th,.compare td{height:24px;padding:0;border-bottom:1.5px solid var(--white)}
  .compare thead th{height:23px;font-size:13px;font-weight:700;color:var(--white);
    text-transform:uppercase;letter-spacing:.2px;border-bottom:4px solid var(--white)}
  .compare .col-feature{width:261px;text-align:left;padding-left:22px}
  .compare .col-wax{width:171px}
  .compare .col-ceramic{width:158px}
  .compare .col-ppf{width:194px}
  .compare thead th.col-feature{background:var(--navy)}
  .compare thead th.col-wax{background:linear-gradient(90deg,var(--wax),var(--wax-light),var(--wax));color:var(--navy)}
  .compare thead th.col-ceramic{background:var(--navy)}
  .compare thead th.col-ppf{background:var(--ppf)}
  .compare tbody th{font-size:10.5px;font-weight:600;color:var(--white);text-align:left;padding-left:22px}
  .compare tbody td{text-align:center;font-size:10.5px;background:var(--cell);vertical-align:middle}
  .compare tbody td.col-ppf{background:var(--cell-alt)}
  .row-core th{background:var(--sky)}
  .row-env th{background:var(--steel)}
  .row-phys th{background:var(--slate)}
  .row-app th{background:var(--navy)}
  .compare tbody .row-app td,.compare tbody .row-app td.col-ppf{background:var(--cell-last)}
  .dot{width:14px;height:14px;display:inline-block;vertical-align:middle}
  .gauge{width:20px;height:20px;display:inline-block;vertical-align:middle}

  .legend{position:absolute;left:58px;top:1091px;display:flex;gap:7px}
  .legend li{list-style:none;height:22px;border-radius:11px;border:1px solid;display:flex;
    align-items:center;gap:6px;padding:0 12px 0 3px;font-size:14.5px;background:var(--white)}
  .legend .lv-low{border-color:var(--yellow);width:65px}
  .legend .lv-med{border-color:var(--green);width:84px}
  .legend .lv-high{border-color:var(--red);width:65px}
  .legend i{width:16px;height:16px;border-radius:50%;display:block;flex:none}
  .lv-low i{background:var(--yellow)}
  .lv-med i{background:var(--green)}
  .lv-high i{background:var(--red)}

  .site{position:absolute;left:425px;top:1083px;width:368px;height:30px;border-radius:7px;
    background:var(--navy);color:var(--white);display:flex;align-items:center;justify-content:center;
    font-size:17px;letter-spacing:4.4px;font-weight:400}
  .site b{font-weight:700}
</style>
</head>
<body>
<svg width="0" height="0" style="position:absolute" aria-hidden="true">
  <defs>
    <symbol id="dot-full-green" viewBox="0 0 20 20"><circle cx="10" cy="10" r="9" fill="#52b51f"/></symbol>
    <symbol id="dot-full-red" viewBox="0 0 20 20"><circle cx="10" cy="10" r="9" fill="#ee1111"/></symbol>
    <symbol id="dot-half-yellow" viewBox="0 0 20 20"><circle cx="10" cy="10" r="9" fill="#fff" stroke="#e4e4e4" stroke-width=".8"/><path d="M10 1A9 9 0 0 1 10 19Z" fill="#f7bf08"/></symbol>
    <symbol id="dot-quarter-yellow" viewBox="0 0 20 20"><circle cx="10" cy="10" r="9" fill="#fff" stroke="#e4e4e4" stroke-width=".8"/><path d="M10 10L10 1A9 9 0 0 1 19 10Z" fill="#f7bf08"/></symbol>
    <symbol id="dot-three-green" viewBox="0 0 20 20"><circle cx="10" cy="10" r="9" fill="#fff" stroke="#52b51f" stroke-width=".8"/><path d="M10 10L19 10A9 9 0 1 1 10 1Z" fill="#52b51f"/></symbol>
    <symbol id="dot-quarter-green" viewBox="0 0 20 20"><circle cx="10" cy="10" r="9" fill="#fff" stroke="#52b51f" stroke-width=".8"/><path d="M10 10L10 1A9 9 0 0 1 19 10Z" fill="#52b51f"/></symbol>
    <symbol id="tick" viewBox="0 0 10 10"><circle cx="5" cy="5" r="5" fill="#111"/><path d="M2.6 5.1L4.3 6.7 7.4 3.5" fill="none" stroke="#fff" stroke-width="1.3"/></symbol>
    <symbol id="gauge-ring" viewBox="0 0 20 20">
      <path d="M4 16A8 8 0 0 1 3.2 6" fill="none" stroke="#52b51f" stroke-width="2.6"/>
      <path d="M3.2 6A8 8 0 0 1 13 2.6" fill="none" stroke="#f7bf08" stroke-width="2.6"/>
      <path d="M13 2.6A8 8 0 0 1 16 16" fill="none" stroke="#ee1111" stroke-width="2.6"/>
      <circle cx="10" cy="10.5" r="5" fill="#fff" stroke="#666" stroke-width=".6"/>
    </symbol>
  </defs>
</svg>

<main class="flyer">
  <svg class="hero-art" viewBox="0 0 909 540" aria-hidden="true">
    <defs>
      <linearGradient id="heroBlue" x1="0" y1="0" x2="1" y2="1">
        <stop offset="0" stop-color="#2166b4"/><stop offset="1" stop-color="#1a57a2"/>
      </linearGradient>
    </defs>
    <polygon points="18,63 568,63 556,81 0,81 0,81" fill="#262626"/>
    <polygon points="0,81 555,81 407,415 0,415" fill="url(#heroBlue)"/>
    <rect x="0" y="415" width="58" height="107" fill="url(#heroBlue)"/>
    <polygon points="572,0 586,0 440,330 426,330" fill="#262626"/>
    <polygon points="880,320 909,320 909,360 868,360" fill="#262626"/>
  </svg>
  <svg class="hero-art" viewBox="0 0 909 540" role="img" aria-label="Photo of a masked technician kneeling beside a red car, machine-polishing the rear door panel">
    <defs>
      <linearGradient id="photoTone" x1="0" y1="0" x2="1" y2="0.4">
        <stop offset="0" stop-color="#2a2c30"/><stop offset=".5" stop-color="#3b3e44"/><stop offset=".72" stop-color="#c81616"/><stop offset="1" stop-color="#e62a22"/>
      </linearGradient>
    </defs>
    <polygon points="601,0 909,0 909,360 860,415 407,415" fill="url(#photoTone)"/>
  </svg>

  <h1 class="title">
    <span class="t-paint">Paint</span>
    <span class="t-protection">Protection</span>
    <span class="t-options">Options</span>
  </h1>

  <section class="cards">
    <article class="card card-ceramic">
      <h2><span class="accent">CERAMIC</span> COATINGS</h2>
      <svg class="thumb" viewBox="0 0 100 111" role="img" aria-label="Close-up of a gloved hand polishing red paint with a rotary buffer">
        <defs><linearGradient id="thumbCeramic" x1="0" y1="0" x2="1" y2="1"><stop offset="0" stop-color="#e42020"/><stop offset=".6" stop-color="#b31414"/><stop offset="1" stop-color="#2b2b2b"/></linearGradient></defs>
        <rect width="100" height="111" fill="url(#thumbCeramic)"/>
      </svg>
      <p class="lead">Ceramic coatings are liquid polymer coatings that bond to a vehicle’s painted surface. The coatings are formulated to retain the show room finish by protecting against corrosion and contaminants like UV damage, oxidation, road salt and acid rain.&nbsp; Ceramic coatings give your car a deep, glossy finish that reflects light and makes your paint look more vibrant while greatly extending the paint's lifespan.</p>
      <p class="body">The chemical bonding process improves color depth and leaves a smooth finish. The hydrophobic (water repellent) properties repel water and dirt as well as protect against damaging pollutants.&nbsp; This makes care and maintenance a breeze while retaining the show room finish.&nbsp; Never wax again!</p>
      <ul class="ticks">
        <li><svg><use href="#tick"/></svg>Enhance and retain showroom finish</li>
        <li><svg><use href="#tick"/></svg>Protect against corrosion and contaminants</li>
        <li><svg><use href="#tick"/></svg>Reduce care and maintenance</li>
      </ul>
    </article>
    <article class="card card-ppf">
      <h2><span class="accent">PAINT PROTECTION</span> FILM (PPF)</h2>
      <svg class="thumb" viewBox="0 0 100 111" role="img" aria-label="Gloved hands stretching clear protection film over a car panel">
        <defs><linearGradient id="thumbPpf" x1="0" y1="0" x2="1" y2="1"><stop offset="0" stop-color="#f1ece4"/><stop offset=".55" stop-color="#d8d0c4"/><stop offset="1" stop-color="#8d8780"/></linearGradient></defs>
        <rect width="100" height="111" fill="url(#thumbPpf)"/>
      </svg>
      <p class="lead">Paint Protection Film (PPF) is a transparent, thermoplastic urethane film that is applied directly to the car’s painted surfaces. PPF excels at shielding your vehicle from rock chips, scratches, and other physical damage. It has self-healing properties that can repair minor scratches and swirl marks over time.</p>
      <p class="body">Paint Protection Film (PPF) is a transparent, thermoplastic urethane film that is applied directly to the car’s painted surfaces. PPF excels at shielding your vehicle from rock chips, scratches, and other physical damage. It has self-healing properties that can repair minor scratches and swirl marks over time.</p>
      <ul class="ticks">
        <li><svg><use href="#tick"/></svg>Protect against rock chips, scratches, and physical damage</li>
        <li><svg><use href="#tick"/></svg>Easily repair minor scratches and swirl marks</li>
        <li><svg><use href="#tick"/></svg>Protect against corrosion and contaminants</li>
      </ul>
    </article>
  </section>

  <table class="compare">
    <thead>
      <tr>
        <th class="col-feature">Feature</th>
        <th class="col-wax">Car Wax</th>
        <th class="col-ceramic">Ceramic Coating</th>
        <th class="col-ppf">Paint Protection Film</th>
      </tr>
    </thead>
    <tbody>
      <tr class="row-core"><th>Duration</th><td>2 - 4 Weeks</td><td>3 - 10 Years</td><td class="col-ppf">7 - 10 Years</td></tr>
      <tr class="row-core"><th>Thickness</th><td>.5 - 1.5 μm</td><td>7 - 10 μm</td><td class="col-ppf">200 - 250 μm</td></tr>
      <tr class="row-core"><th>Gloss Enhancement</th>
        <td><svg class="dot"><use href="#dot-full-green"/></svg></td><td><svg class="dot"><use href="#dot-full-green"/></svg></td><td class="col-ppf"><svg class="dot"><use href="#dot-full-green"/></svg></td></tr>
      <tr class="row-env"><th>Acid Rain Damage</th>
        <td><svg class="dot"><use href="#dot-half-yellow"/></svg></td><td><svg class="dot"><use href="#dot-full-green"/></svg></td><td class="col-ppf"><svg class="dot"><use href="#dot-full-green"/></svg></td></tr>
      <tr class="row-env"><th>Corrosion Prevention</th>
        <td><svg class="dot"><use href="#dot-half-yellow"/></svg></td><td><svg class="dot"><use href="#dot-full-green"/></svg></td><td class="col-ppf"><svg class="dot"><use href="#dot-full-green"/></svg></td></tr>
      <tr class="row-env"><th>UV/Oxidation Protection</th>
        <td><svg class="dot"><use href="#dot-half-yellow"/></svg></td><td><svg class="dot"><use href="#dot-full-green"/></svg></td><td class="col-ppf"><svg class="dot"><use href="#dot-full-green"/></svg></td></tr>
      <tr class="row-env"><th>Hard Water Damage</th>
        <td><svg class="dot"><use href="#dot-quarter-yellow"/></svg></td><td><svg class="dot"><use href="#dot-three-green"/></svg></td><td class="col-ppf"><svg class="dot"><use href="#dot-full-green"/></svg></td></tr>
      <tr class="row-env"><th>Insect Splatter Damage</th>
        <td><svg class="dot"><use href="#dot-quarter-yellow"/></svg></td><td><svg class="dot"><use href="#dot-three-green"/></svg></td><td class="col-ppf"><svg class="dot"><use href="#dot-full-green"/></svg></td></tr>
      <tr class="row-phys"><th>Chip Protection</th>
        <td><svg class="dot"><use href="#dot-full-red"/></svg></td><td><svg class="dot"><use href="#dot-quarter-green"/></svg></td><td class="col-ppf"><svg class="dot"><use href="#dot-full-green"/></svg></td></tr>
      <tr class="row-phys"><th>Scratch Protection</th>
        <td><svg class="dot"><use href="#dot-full-red"/></svg></td><td><svg class="dot"><use href="#dot-quarter-green"/></svg></td><td class="col-ppf"><svg class="dot"><use href="#dot-full-green"/></svg></td></tr>
      <tr class="row-phys"><th>Swirl Protection</th>
        <td><svg class="dot"><use href="#dot-full-red"/></svg></td><td><svg class="dot"><use href="#dot-full-red"/></svg></td><td class="col-ppf"><svg class="dot"><use href="#dot-full-green"/></svg></td></tr>
      <tr class="row-app"><th>Application Complexity</th>
        <td><svg class="gauge" viewBox="0 0 20 20"><use href="#gauge-ring"/><text x="10" y="12.6" font-size="6" font-family="Poppins,sans-serif" font-weight="600" text-anchor="middle" fill="#333">L</text></svg></td>
        <td><svg class="gauge" viewBox="0 0 20 20"><use href="#gauge-ring"/><text x="10" y="12.6" font-size="6" font-family="Poppins,sans-serif" font-weight="600" text-anchor="middle" fill="#333">M</text></svg></td>
        <td class="col-ppf"><svg class="gauge" viewBox="0 0 20 20"><use href="#gauge-ring"/><text x="10" y="12.6" font-size="6" font-family="Poppins,sans-serif" font-weight="600" text-anchor="middle" fill="#333">H</text></svg></td></tr>
    </tbody>
  </table>

  <ul class="legend">
    <li class="lv-low"><i></i>Low</li>
    <li class="lv-med"><i></i>Medium</li>
    <li class="lv-high"><i></i>High</li>
  </ul>

  <div class="site">www.<b>shieldcoatdetail</b>.com</div>
</main>
</body>
</html>
```